Launch of a new Investment fund

Im looking for someone design a logo and website for my Investment fund located in Singapore.

Attached to this project you will find a project scope document that details exactly what i am looking for and also includes a website copy that i have written up. I am happy for you to take your own inspiration as well to design the website. At this stage the website wont be very detailed as there isn't much information to showcase. I will require the website to be easily editable in the future so i can update it with progress the fund makes.

If you require any further details on the project please reach out to me

Coding

Coded - Design and coding required

Number of Pages Required

4 page

```html
<!DOCTYPE html>
<html lang="en">
<head>
<meta charset="utf-8">
<title>Altura Ridge Capital Management</title>
<link href="https://fonts.googleapis.com/css2?family=Josefin+Sans:wght@600;700&family=Jost:wght@400;500;600&display=swap" rel="stylesheet">
<style>
:root{
  --navy:#0f0d24;
  --navy-btn:#213a86;
  --blue:#3a66f0;
  --blue-bar:#2c4eb0;
  --ink:#141414;
  --muted:#6b6b78;
  --light:#eef0f5;
  --white:#ffffff;
  --line:#d9dbe3;
  --icon-box:#5d5f66;
}
*{box-sizing:border-box;margin:0;padding:0}
html,body{width:1200px;height:3231px;overflow:hidden}
body{font-family:"Jost",sans-serif;color:var(--ink);background:var(--white);position:relative}
section,header,footer{position:absolute;left:0;width:1200px}
.abs{position:absolute}
.heading{font-family:"Josefin Sans",sans-serif;font-weight:700;text-transform:uppercase;letter-spacing:.5px}
.btn{position:absolute;display:flex;align-items:center;justify-content:center;color:var(--white);font-size:10.5px;font-weight:600;letter-spacing:.4px;text-transform:uppercase}

/* header */
.site-header{top:0;height:77px;background:var(--white)}
.brand{display:flex;align-items:center;gap:10px}
.brand-mark{width:30px;height:30px;background:var(--blue);flex:none}
.brand-text{display:flex;flex-direction:column;line-height:1.05}
.brand-name{font-family:"Jost",sans-serif;font-weight:600;font-size:17px;color:var(--navy-btn);letter-spacing:.3px}
.brand-sub{font-family:"Jost",sans-serif;font-weight:600;font-size:10px;color:var(--navy-btn);letter-spacing:2px}
.nav a{position:absolute;top:33px;font-size:10.5px;font-weight:500;color:var(--ink);text-decoration:none;letter-spacing:.3px}
.nav a.active{color:var(--blue);text-decoration:underline}
.divider{position:absolute;top:0;width:1px;height:77px;background:var(--line)}
.social-dot{position:absolute;width:14px;height:14px;border-radius:50%;background:#3a3a44}
.help{position:absolute;left:930px;top:24px;font-size:9px;color:var(--ink);line-height:1.35}
.help b{font-size:11.5px;font-weight:600}

/* hero */
.hero{top:77px;height:534px;overflow:hidden}
.hero-photo{position:absolute;inset:0;background:linear-gradient(100deg,#4a5563 0%,#68717d 40%,#7a7f88 60%,#4b5060 100%)}
.hero-shade{position:absolute;inset:0;background:linear-gradient(90deg,rgba(15,13,36,.55),rgba(15,13,36,.15))}
.hero-title{position:absolute;left:149px;top:196px;color:var(--white);font-size:45px;line-height:50px}

/* what we do */
.what{top:611px;height:480px;background:var(--navy);color:var(--white)}
.photo{position:absolute}
.what-title{position:absolute;left:701px;top:108px;font-size:30px}
.what-copy{position:absolute;left:701px;top:162px;width:352px;font-size:12px;line-height:16.3px;color:#e6e6ee}
.what-copy p+p{margin-top:13px}

/* founder */
.founder{top:1091px;height:479px;background:var(--white)}
.founder-title{position:absolute;left:149px;top:103px;font-size:30px}
.founder-lead{position:absolute;left:149px;top:150px;font-size:12.5px;font-weight:500;color:var(--blue);line-height:16.5px}
.founder-copy{position:absolute;left:149px;top:198px;width:434px;font-size:12px;line-height:16.3px;color:var(--muted)}
.badge{position:absolute;left:665px;top:267px;width:99px;height:88px;background:var(--blue);border:3px solid var(--white);outline:2px solid var(--blue);color:var(--white);text-align:center;padding-top:8px}
.badge .num{font-family:"Josefin Sans",sans-serif;font-weight:700;font-size:30px;line-height:30px}
.badge .yr{font-size:14px;line-height:15px}
.badge .ex{font-size:8px;letter-spacing:.5px;text-transform:uppercase}

/* investments */
.investments{top:1570px;height:558px;background:var(--light)}
.inv-title{position:absolute;width:100%;text-align:center;top:70px;font-size:30px}
.inv-sub{position:absolute;width:100%;text-align:center;top:118px;font-size:12px;line-height:16.5px;color:var(--muted)}
.icon-box{position:absolute;width:78px;height:72px;background:var(--icon-box);border:3px solid var(--white);display:flex;align-items:center;justify-content:center}
.inv-item{position:absolute;width:230px}
.inv-item h3{font-size:13.5px;font-weight:600;color:var(--blue);text-transform:uppercase;letter-spacing:.3px;margin-bottom:6px}
.inv-item p{font-size:10.5px;line-height:14.2px;color:var(--muted)}

/* partners */
.partners{top:2128px;height:381px;background:var(--navy)}
.partners-title{position:absolute;width:100%;text-align:center;top:70px;font-size:30px;color:var(--white)}
.partner-card{position:absolute;top:136px;width:165px;height:102px;background:var(--white);display:flex;align-items:center;justify-content:center}
.arrow{position:absolute;top:276px;width:30px;height:29px;display:flex;align-items:center;justify-content:center}

/* inquiry */
.inquiry{top:2509px;height:425px;background:var(--white)}
.inq-title{position:absolute;width:100%;text-align:center;top:74px;font-size:30px}
.field-label{position:absolute;font-size:8.5px;font-weight:500;text-transform:uppercase;color:var(--ink)}
.field{position:absolute;border:1px solid var(--line);background:var(--white)}
.field svg{position:absolute;left:10px;top:10px}

/* footer */
.site-footer{top:2934px;height:259px;background:var(--navy);color:var(--white)}
.foot-brand{position:absolute;left:149px;top:72px;width:155px;display:flex;flex-direction:column;align-items:center;gap:10px;text-align:center}
.foot-brand .brand-mark{width:40px;height:40px}
.foot-brand .brand-name{color:var(--white);font-size:16px;line-height:1.1}
.foot-brand .brand-sub{color:var(--white);font-size:11px}
.foot-col h4{font-size:14px;font-weight:600;color:var(--blue);text-transform:uppercase;letter-spacing:.4px;margin-bottom:12px}
.foot-col{position:absolute;top:57px;font-size:11px;line-height:15px}
.contact-row{display:flex;gap:10px;margin-bottom:14px}
.links li{list-style:none;margin-bottom:6.5px}
.links li.active{color:var(--blue);text-decoration:underline}
.news-input{position:absolute;left:813px;top:123px;width:238px;height:30px;border:1px solid #3a3a55;font-size:10.5px;color:#9a9ab0;padding:8px 18px}
.bottom-bar{position:absolute;left:0;top:3193px;width:1200px;height:38px;background:var(--blue-bar);color:#e6eaff;font-size:10.5px}
.bottom-bar .social-dot{background:#c9d3ff}
</style>
</head>
<body>

<header class="site-header">
  <div class="brand abs" style="left:149px;top:19px">
    <span class="brand-mark"></span>
    <span class="brand-text"><span class="brand-name">ALTURA RIDGE CAPITAL</span><span class="brand-sub">MANAGEMENT</span></span>
  </div>
  <nav class="nav">
    <a class="active" style="left:475px">HOME</a>
    <a style="left:532px">ABOUT US</a>
    <a style="left:608px">INVESTMENTS</a>
    <a style="left:706px">CONTACT US</a>
  </nav>
  <span class="divider" style="left:811px"></span>
  <span class="social-dot" style="left:828px;top:32px" role="img" aria-label="Profile link"></span>
  <span class="social-dot" style="left:852px;top:32px" role="img" aria-label="Feed link"></span>
  <span class="divider" style="left:885px"></span>
  <svg class="abs" style="left:900px;top:27px" width="24" height="24" viewBox="0 0 24 24"><circle cx="12" cy="12" r="12" fill="var(--blue)"/><path d="M8 7c1 0 1.5 2 1.5 2.5S8.5 11 8.5 11s1 2.5 4.5 4.5c0 0 1-1 1.5-1S17 15 17 16s-1 1.5-2 1.5C10 17 7 12 7 8.5 7 7.5 7.5 7 8 7z" fill="#fff"/></svg>
  <div class="help">Need help? Talk to an expert<br><b>+65 6123 4567</b></div>
</header>

<section class="hero">
  <div class="hero-photo" role="img" aria-label="Business team meeting around a table reviewing documents"></div>
  <div class="hero-shade"></div>
  <svg class="abs" style="left:0;top:0" width="1200" height="534" viewBox="0 0 1200 534">
    <polygon points="760,0 960,0 860,180" fill="#ffffff" fill-opacity=".12"/>
    <polygon points="880,0 1000,0 940,110" fill="#ffffff" fill-opacity=".1"/>
    <polygon points="1200,0 1200,534 770,534" fill="#1f3fb8" fill-opacity=".75"/>
    <polygon points="1170,0 1200,0 1200,60" fill="#1f3fb8" fill-opacity=".75"/>
  </svg>
  <h1 class="hero-title heading">Passion for<br>uncovering new<br>opportunities</h1>
</section>

<section class="what">
  <div class="photo" style="left:149px;top:75px;width:319px;height:329px;background:linear-gradient(160deg,#9fc4de 0%,#3f8aa0 45%,#b0566f 75%,#2c6f80 100%)" role="img" aria-label="Container ship loaded with cargo at a port"></div>
  <div class="photo" style="left:362px;top:143px;width:266px;height:235px;background:linear-gradient(135deg,#f4f5f7 0%,#d9dde3 55%,#8fa3b8 100%);border:3px solid var(--white)" role="img" aria-label="Scientist examining samples with a microscope"></div>
  <h2 class="what-title heading">What we do</h2>
  <div class="what-copy">
    <p>A beacon of innovative investment where strategic diversification meets meticulous market comprehension. We navigate the complexities of Global Equities, Real Estate, Venture Capital, Private Equity, and Alternative Assets, focusing on uncovering distinctive investment opportunities for our investors.</p>
    <p>At Altura Ridge, investment is not just a transaction; it's a carefully orchestrated process, mirroring the meticulous management of personal assets.</p>
  </div>
  <span class="btn" style="left:701px;top:337px;width:109px;height:36px;background:var(--blue)">Read more</span>
</section>

<section class="founder">
  <h2 class="founder-title heading">Meet our founder</h2>
  <p class="founder-lead">Meet Theo, the driving force behind<br>Altura Ridge Capital Management.</p>
  <p class="founder-copy">From co-founding a regional clean energy business to pioneering ventures in diverse sectors, Theo's entrepreneurial journey is marked by a passion for market innovation and sustainable growth. With over a decade of diverse business scaling experience, Theo established Altura Ridge Capital, evolving from personal investment to a trust-fortified endeavour of market innovation and niche investment exploration.</p>
  <span class="btn" style="left:149px;top:324px;width:98px;height:36px;background:var(--navy-btn)">Profile</span>
  <div class="photo" style="left:731px;top:75px;width:320px;height:323px;background:linear-gradient(160deg,#b9b3a6 0%,#8c8a80 40%,#2f3b4c 75%,#25303f 100%)" role="img" aria-label="Portrait of the founder in a suit outdoors"></div>
  <div class="badge"><div class="num">15+</div><div class="yr">Years of</div><div class="ex">Experience</div></div>
</section>

<section class="investments">
  <h2 class="inv-title heading">Investments</h2>
  <p class="inv-sub">Altura Ridge's portfolio showcases our ability to identify undervalued opportunities with<br>significant growth potential.</p>
  <div class="photo" style="left:438px;top:179px;width:324px;height:304px;background:linear-gradient(135deg,#6b4a36 0%,#b78c6c 45%,#e6d8c8 75%,#8a6b55 100%)" role="img" aria-label="Smiling clients shaking hands with an advisor"></div>

  <div class="icon-box" style="left:401px;top:234px"><svg width="30" height="30" viewBox="0 0 30 30" fill="none" stroke="#fff" stroke-width="1.6"><circle cx="17" cy="9" r="6"/><path d="M3 22h6l5 2 8-5M3 27h7l6 1 11-7"/></svg></div>
  <div class="icon-box" style="left:401px;top:353px"><svg width="30" height="30" viewBox="0 0 30 30" fill="none" stroke="#fff" stroke-width="1.6"><path d="M18 4a10 10 0 1 1-10 10h10z"/><path d="M14 2v9H5"/><rect x="3" y="20" width="6" height="7"/></svg></div>
  <div class="icon-box" style="left:720px;top:234px"><svg width="30" height="30" viewBox="0 0 30 30" fill="none" stroke="#fff" stroke-width="1.6"><circle cx="15" cy="15" r="12"/><path d="M8 19v-5M12 19v-8M16 19v-3"/><circle cx="21" cy="19" r="4"/></svg></div>
  <div class="icon-box" style="left:720px;top:353px"><svg width="30" height="30" viewBox="0 0 30 30" fill="none" stroke="#fff" stroke-width="1.6"><path d="M3 17l10-9 10 9M6 15v11h14V15"/><rect x="11" y="19" width="4" height="7"/><circle cx="24" cy="6" r="3"/></svg></div>

  <div class="inv-item" style="left:149px;top:231px"><h3>Venture capital</h3><p>Strategic investments in venture capital, where we harness our industry contacts and market understanding to invest in high growth startups and businesses.</p></div>
  <div class="inv-item" style="left:149px;top:349px"><h3>Private equity</h3><p>Access to investments in cutting edge sectors, featuring companies like Norvale AI, Chatterbay, Pixelwave, Datagrove, Orbitek, Synapta, Freightory, Cortexa Systems and Brightforge Games</p></div>
  <div class="inv-item" style="left:819px;top:231px"><h3>Global equity markets</h3><p>We've demonstrated exceptional skill in identifying undervalued stocks and markets with high growth potential, leveraging in-depth research and market analysis</p></div>
  <div class="inv-item" style="left:819px;top:361px"><h3>Property development</h3><p>Curated development projects, exemplifying our ability to identify and capitalise on high-value real estate opportunities</p></div>
</section>

<section class="partners">
  <h2 class="partners-title heading">Our partners</h2>
  <div class="partner-card" style="left:149px"><svg width="110" height="36"><circle cx="18" cy="18" r="16" fill="#6cc36a"/><rect x="42" y="12" width="64" height="12" fill="#8a8d96"/></svg></div>
  <div class="partner-card" style="left:333px"><svg width="110" height="36"><rect x="3" y="3" width="30" height="30" fill="#f2a33a"/><rect x="42" y="12" width="64" height="12" fill="#8a8d96"/></svg></div>
  <div class="partner-card" style="left:518px"><svg width="110" height="36"><circle cx="18" cy="18" r="16" fill="#2a9fd8"/><rect x="42" y="12" width="64" height="12" fill="#8a8d96"/></svg></div>
  <div class="partner-card" style="left:702px"><svg width="110" height="36"><circle cx="18" cy="18" r="16" fill="#e23b3b"/><rect x="42" y="12" width="64" height="12" fill="#8a8d96"/></svg></div>
  <div class="partner-card" style="left:886px"><svg width="110" height="36"><rect x="3" y="8" width="32" height="20" fill="#2aa6b8"/><rect x="42" y="12" width="64" height="12" fill="#8a8d96"/></svg></div>
  <div class="arrow" style="left:567px;background:var(--blue)"><svg width="12" height="10" viewBox="0 0 12 10" fill="none" stroke="#fff" stroke-width="1.6"><path d="M11 5H1M5 1 1 5l4 4"/></svg></div>
  <div class="arrow" style="left:603px;background:var(--navy-btn)"><svg width="12" height="10" viewBox="0 0 12 10" fill="none" stroke="#fff" stroke-width="1.6"><path d="M1 5h10M7 1l4 4-4 4"/></svg></div>
</section>

<section class="inquiry">
  <h2 class="inq-title heading">Quick inquiry</h2>
  <span class="field-label" style="left:262px;top:134px">Name</span>
  <span class="field-label" style="left:494px;top:134px">Your email</span>
  <span class="field-label" style="left:725px;top:134px">Phone number</span>
  <div class="field" style="left:262px;top:148px;width:213px;height:32px"><svg width="10" height="11" fill="none" stroke="#8a8d96"><circle cx="5" cy="3.5" r="2.5"/><path d="M1 10c0-3 8-3 8 0"/></svg></div>
  <div class="field" style="left:494px;top:148px;width:212px;height:32px"><svg width="12" height="10" fill="none" stroke="#8a8d96"><rect x=".5" y="1.5" width="10" height="7"/><path d="M.5 1.5l5 4 5-4"/></svg></div>
  <div class="field" style="left:725px;top:148px;width:212px;height:32px"><svg width="8" height="11" fill="none" stroke="#8a8d96"><rect x=".5" y=".5" width="6" height="10" rx="1"/></svg></div>
  <span class="field-label" style="left:262px;top:200px">Your message</span>
  <div class="field" style="left:262px;top:211px;width:675px;height:77px"><svg width="10" height="10" fill="none" stroke="#8a8d96"><path d="M.5 .5h9v6l-3 3h-6z"/></svg></div>
  <span class="btn" style="left:557px;top:315px;width:86px;height:35px;background:var(--blue)">Submit</span>
</section>

<footer class="site-footer">
  <div class="foot-brand">
    <span class="brand-mark"></span>
    <span class="brand-text"><span class="brand-name">ALTURA RIDGE CAPITAL</span><span class="brand-sub">MANAGEMENT</span></span>
  </div>

  <div class="foot-col" style="left:392px">
    <h4>Contact info</h4>
    <div class="contact-row"><svg width="12" height="14" viewBox="0 0 12 14"><path d="M6 0a5 5 0 0 1 5 5c0 4-5 9-5 9S1 9 1 5a5 5 0 0 1 5-5z" fill="var(--blue)"/><circle cx="6" cy="5" r="2" fill="var(--navy)"/></svg><span>28 Harbourfront Walk,<br>Singapore 098765</span></div>
    <div class="contact-row"><svg width="12" height="12" viewBox="0 0 24 24"><path d="M5 2c2 0 3 4 3 5s-2 3-2 3 2 5 8 8c0 0 2-2 3-2s5 1 5 3-2 3-4 3C9 22 2 15 2 6c0-2 1-4 3-4z" fill="var(--blue)"/></svg><span>+65 6123 4567</span></div>
    <div class="contact-row"><svg width="12" height="12" viewBox="0 0 12 12"><rect x="0" y="2" width="12" height="8" fill="var(--blue)"/><path d="M0 2l6 5 6-5" stroke="var(--navy)" fill="none"/></svg><span>info@alturaridgecapital.com</span></div>
    <div class="contact-row"><svg width="12" height="12" viewBox="0 0 12 12"><circle cx="6" cy="6" r="5.5" fill="var(--blue)"/></svg><span>Live location</span></div>
  </div>

  <div class="foot-col" style="left:652px">
    <h4>Quick link</h4>
    <ul class="links">
      <li class="active">Home</li>
      <li>About Us</li>
      <li>Investments</li>
      <li>Contact Us</li>
      <li>Terms of Use</li>
      <li>Privacy Policy</li>
    </ul>
  </div>

  <div class="foot-col" style="left:813px;width:240px">
    <h4>Stay in touch</h4>
    <p>Subscribe to our newsletter and<br>stay updated</p>
  </div>
  <div class="news-input">Your email address*</div>
  <span class="btn" style="left:813px;top:166px;width:121px;height:31px;background:var(--blue)">Subscribe now</span>
</footer>

<div class="bottom-bar">
  <span class="abs" style="left:149px;top:12px">© 2024 Altura Ridge Capital Management. All Right Reserved</span>
  <span class="social-dot" style="left:1006px;top:12px" role="img" aria-label="Profile link"></span>
  <span class="social-dot" style="left:1036px;top:12px" role="img" aria-label="Feed link"></span>
</div>

</body>
</html>
```